refurbishment of diamond cut alloy wheels

we need to design a flyer that will catch the eye of the customer to refurbish diamond cut alloy wheels. we refurbish the wheels by using the latest CNC machine to precision cut and resurface the wheel. we would like before and after pictures of maybe Valtorin, KRZ, Ovel wheels to give it a prestige look. The final design should communicate an expensive look and providing a good image for the business. The colours that I would like to use is black and red which should make the flyer stand out. The logo must sit on a black background without the wordings of specialists in TQ, Ovel etc and also without servicing, diagnostics etc as well. This flyer is just to communicate refurbishment of alloy wheels to high standard.

Target Market(s)

any members of the public and car dealerships

Industry/Entity Type

Automotive

Colors

Designer to choose colors to be used in the design.

Requirements
Must have
• Wow factor with great images of wheels
Nice to have
• Maybe on the front of the flyer it has a picture of a wheel and then on the back of the flyer it has before and after pictures to show how just how incredible it is to refurbish wheels
Should not have
• other makes of wheels apart from KRZ, Ovel, and any other high end makes of vehicles wheels

```html
<!DOCTYPE html>
<html lang="en">
<head>
<meta charset="utf-8">
<title>Halden Motors – Alloy Wheel Refurbishment Flyer</title>
<link href="https://fonts.googleapis.com/css2?family=Kanit:wght@300;400;500&family=Russo+One&display=swap" rel="stylesheet">
<style>
  :root {
    --canvas: #e9e7e5;
    --black: #050505;
    --deep-red: #6e0710;
    --red: #a3111c;
    --bright-red: #c8202a;
    --white: #ffffff;
    --soft-white: #ececec;
    --gold: #d9b24a;
    --frame: #d8d8d8;
  }
  * { box-sizing: border-box; margin: 0; padding: 0; }
  html, body { width: 926px; height: 1200px; overflow: hidden; }
  body {
    background: var(--canvas);
    font-family: "Kanit", sans-serif;
    position: relative;
  }
  .page {
    position: absolute;
    top: 310px;
    width: 409px;
    height: 579px;
    overflow: hidden;
    box-shadow: 6px 8px 12px rgba(0,0,0,0.35);
  }
  .page-front { left: 42px; background: linear-gradient(180deg, var(--black) 0%, #2a0508 30%, var(--red) 70%, var(--deep-red) 100%); }
  .page-back { left: 483px; background: linear-gradient(180deg, var(--black) 0%, var(--black) 45%, var(--deep-red) 75%, var(--red) 100%); }

  .brand {
    display: flex; align-items: center; gap: 6px;
    color: var(--white);
    font-family: "Kanit", sans-serif;
    font-weight: 500;
    font-size: 17px;
    letter-spacing: 0.5px;
    text-transform: uppercase;
  }
  .brand-mark { width: 20px; height: 20px; background: var(--bright-red); }

  .front-brand { position: absolute; top: 40px; left: 0; right: 0; justify-content: center; }
  .wheel-photo {
    position: absolute; left: 0; top: 215px; width: 409px; height: 364px;
    background: radial-gradient(circle at 45% 55%, #8a8a8a 0%, #4a4a4a 30%, #1a1a1a 55%, rgba(90,10,15,0.6) 80%, var(--red) 100%);
  }
  .front-title {
    position: absolute; top: 103px; left: 0; right: 0;
    text-align: center;
    font-family: "Russo One", sans-serif;
    font-style: italic;
    color: var(--white);
    font-size: 30px;
    line-height: 35px;
    letter-spacing: 1px;
    transform: skewX(-10deg);
    text-shadow: 0 2px 4px rgba(0,0,0,0.7);
    text-transform: uppercase;
  }

  .back-title {
    position: absolute; top: 30px; left: 0; right: 0;
    text-align: center;
    color: var(--white);
    font-weight: 500;
    font-size: 16.5px;
    line-height: 22px;
    letter-spacing: 0.4px;
    text-transform: uppercase;
  }
  .back-copy {
    position: absolute; top: 94px; left: 46px; right: 46px;
    text-align: center;
    color: var(--soft-white);
    font-weight: 300;
    font-size: 7.4px;
    line-height: 13.5px;
  }
  .back-copy p + p { margin-top: 13px; }

  .compare {
    position: absolute; top: 241px; left: 50px; width: 301px; height: 209px;
    border: 1px solid var(--frame);
    padding: 6px;
    display: flex; gap: 3px;
    background: rgba(0,0,0,0.5);
  }
  .compare-shot { flex: 1; position: relative; }
  .compare-before { background: radial-gradient(circle at 50% 55%, #d4d4d4 0%, #8d8d8d 45%, #2b2b2b 75%, #5a5040 100%); }
  .compare-after { background: radial-gradient(circle at 50% 55%, #e6e6e6 0%, #a8a8a8 45%, #262626 75%, #5a5040 100%); }
  .compare-label {
    position: absolute; top: 2px; left: 4px;
    font-family: "Times New Roman", serif;
    color: var(--gold);
    font-size: 9.5px;
    text-transform: uppercase;
  }

  .back-brand { position: absolute; top: 508px; left: 62px; }

  .contact {
    position: absolute; top: 469px; left: 233px;
    color: var(--white);
    font-weight: 400;
    font-size: 8.6px;
    line-height: 13.5px;
  }
  .contact-lines { list-style: none; margin-top: 14px; }
  .contact-lines li { display: flex; align-items: center; gap: 5px; }
  .contact-lines svg { width: 8px; height: 8px; fill: var(--white); }
</style>
</head>
<body>

<section class="page page-front">
  <div class="brand front-brand"><span class="brand-mark"></span>Halden Motors</div>
  <div class="wheel-photo" role="img" aria-label="Close-up photograph of a polished diamond cut five-spoke alloy wheel with orange brake calipers on a red car"></div>
  <h1 class="front-title">Refurbish<br>Diamond Cut<br>Alloy Wheels</h1>
</section>

<section class="page page-back">
  <h2 class="back-title">Alloy Refurbishment Specialists<br>in and around Ashbury</h2>
  <div class="back-copy">
    <p>If you are looking to refresh the look of your car but don't want the expense of new alloys, with a wide range of limited edition colours to choose from why not consider customising and refurbishing your existing alloys?</p>
    <p>If you've had your alloy wheels long enough for them to require alloy refurbishment you can choose from a wide range of colours for refurbishment or choose a brand new set from our comprehensive range. At Crestline Wheels &amp; Tyres, we stock an extensive range of the latest designs from all the leading suppliers and manufacturers so you are sure to find a stylish new design.</p>
  </div>

  <div class="compare">
    <div class="compare-shot compare-before" role="img" aria-label="Photograph of a worn, scuffed multi-spoke alloy wheel before refurbishment">
      <span class="compare-label">Before</span>
    </div>
    <div class="compare-shot compare-after" role="img" aria-label="Photograph of the same multi-spoke alloy wheel restored to a bright finish after refurbishment">
      <span class="compare-label">After</span>
    </div>
  </div>

  <div class="brand back-brand"><span class="brand-mark"></span>Halden Motors</div>

  <address class="contact" style="font-style:normal">
    14B Marsh Lane,<br>Fenwick, Ashbury,<br>Wessex, AB4 2QT
    <ul class="contact-lines">
      <li><svg viewBox="0 0 10 10" aria-hidden="true"><path d="M2 0.5 L3.6 0.5 L4.3 2.8 L3.2 3.8 Q4.3 5.9 6.2 6.8 L7.2 5.7 L9.5 6.4 L9.5 8 Q9.5 9.5 8 9.5 Q1.5 9 0.5 2 Q0.5 0.5 2 0.5 Z"/></svg>01632 960418</li>
      <li><svg viewBox="0 0 10 10" aria-hidden="true"><path d="M2.5 0.5 H7.5 V3 H2.5 Z M0.5 3.5 H9.5 V8 H8 V6 H2 V8 H0.5 Z M2.5 6.5 H7.5 V9.5 H2.5 Z"/></svg>01632 960772</li>
      <li><svg viewBox="0 0 10 10" aria-hidden="true"><path d="M0.5 2 H9.5 V8.5 H0.5 Z M0.8 2.3 L5 5.6 L9.2 2.3" stroke="#000" stroke-width="0.6"/></svg>hello@haldenmotors.example</li>
    </ul>
  </address>
</section>

</body>
</html>
```